Mobile technology Business Card Design Project

We need a business card design for our company based in Sydeny Australia, that takes a company's desktop sites and creates a mobile site compatible to all mobile/smartphone devices. This allows greater ease of use and generally faster business conversion than customers using a desktop site.
Our company is called Zelvora but we refer to it as Zelvora Solutions. If this could be represented somewhere on the business card that would be great.
Am open to suggestions regarding the colours but a high tech  theme would be good.
Happy bidding!

Target Market(s)
Business owner that has a website and is reasonably savvy regarding online/mobile marketing.
Industry/Entity Type
Business
Requirements
Must have
- Business card details:
Director Peter Hawkley
Address: 4/15 Brenton rd, Kelmore. 2047
Email: tbc
Web: www.zelvora-example.com.au
The cards need to have two different names for the two directors.
Damien Ferrowe & Peter Hawkley (two separate business cards)

```html
<!DOCTYPE html>
<html lang="en">
<head>
<meta charset="utf-8">
<title>Zelvora – Business Cards</title>
<link rel="stylesheet" href="https://fonts.googleapis.com/css2?family=Open+Sans:wght@400;600&family=Oswald:wght@500&display=swap">
<style>
  :root {
    --sky-blue: #1e9ad6;
    --tab-blue: #2a9fdc;
    --sunset-orange: #f29422;
    --tagline-gold: #c8901b;
    --ink: #2b2b2b;
    --white: #ffffff;
    --page: #ffffff;
    --card-shadow: 0 6px 18px rgba(0, 0, 0, 0.22);
  }
  html, body {
    margin: 0;
    width: 1200px;
    height: 969px;
    overflow: hidden;
    background: var(--page);
    font-family: "Open Sans", Arial, sans-serif;
  }
  .sheet { position: relative; width: 1200px; height: 969px; }

  .card {
    position: absolute;
    width: 500px;
    height: 326px;
    border-radius: 22px;
    overflow: hidden;
    box-shadow: var(--card-shadow);
  }

  /* Front */
  .card--front {
    left: 350px; top: 110px;
    background:
      radial-gradient(ellipse 44% 58% at 50% 44%, var(--white) 0%, var(--white) 42%, rgba(255,255,255,0) 100%),
      var(--sky-blue);
    text-align: center;
  }
  .brand-dot {
    display: block;
    border-radius: 50%;
    background: var(--sunset-orange);
  }
  .card--front .brand-dot {
    width: 96px; height: 96px;
    margin: 58px auto 18px;
  }
  .brand-name {
    margin: 0;
    font-weight: 400;
    color: var(--ink);
    line-height: 1;
  }
  .card--front .brand-name { font-size: 46px; letter-spacing: 1px; }
  .tagline {
    margin: 10px 0 0;
    font-size: 19px;
    font-weight: 600;
    color: var(--tagline-gold);
    letter-spacing: 0.5px;
  }

  /* Backs */
  .card--back {
    top: 520px;
    background:
      radial-gradient(ellipse 40% 62% at 18% 32%, var(--white) 0%, var(--white) 45%, rgba(255,255,255,0) 100%),
      var(--sunset-orange);
  }
  .card--peter { left: 70px; }
  .card--damien { left: 630px; }

  .back-brand {
    position: absolute;
    left: 28px; top: 34px;
    width: 160px;
    text-align: center;
  }
  .back-brand .brand-dot { width: 84px; height: 84px; margin: 0 auto 12px; }
  .back-brand .brand-name { font-size: 30px; }

  .holder {
    position: absolute;
    right: 26px; top: 22px;
    text-align: right;
    color: var(--white);
    font-family: "Oswald", "Arial Narrow", sans-serif;
    font-weight: 500;
    line-height: 1.1;
  }
  .holder__name { margin: 0; font-size: 24px; }
  .holder__role { margin: 0; font-size: 16px; }

  .address {
    position: absolute;
    left: 0; right: 0; top: 254px;
    margin: 0;
    text-align: center;
    font-size: 15px;
    color: var(--white);
  }
  .web-tab {
    position: absolute;
    left: 112px; bottom: 0;
    width: 276px; height: 34px;
  }
  .web-tab svg { position: absolute; inset: 0; }
  .web-tab span {
    position: relative;
    display: block;
    line-height: 34px;
    text-align: center;
    font-size: 15px;
    color: var(--white);
  }
</style>
</head>
<body>
<main class="sheet">

  <section class="card card--front" aria-label="Card front">
    <span class="brand-dot" aria-hidden="true"></span>
    <h1 class="brand-name">Zelvora</h1>
    <p class="tagline">Making Sites Go Handheld</p>
  </section>

  <section class="card card--back card--peter" aria-label="Card back, Peter Hawkley">
    <div class="back-brand">
      <span class="brand-dot" aria-hidden="true"></span>
      <p class="brand-name">Zelvora</p>
    </div>
    <div class="holder">
      <p class="holder__name">Peter Hawkley</p>
      <p class="holder__role">Director</p>
    </div>
    <p class="address">4/15 Brenton rd, Kelmore. 2047 Email: tbc</p>
    <div class="web-tab">
      <svg width="276" height="34" viewBox="0 0 276 34" aria-hidden="true"><polygon points="14,0 276,0 262,34 0,34" fill="var(--tab-blue)"/></svg>
      <span>Web: www.zelvora-example.com.au</span>
    </div>
  </section>

  <section class="card card--back card--damien" aria-label="Card back, Damien Ferrowe">
    <div class="back-brand">
      <span class="brand-dot" aria-hidden="true"></span>
      <p class="brand-name">Zelvora</p>
    </div>
    <div class="holder">
      <p class="holder__name">Damien Ferrowe</p>
      <p class="holder__role">Director</p>
    </div>
    <p class="address">4/15 Brenton rd, Kelmore. 2047 Email: tbc</p>
    <div class="web-tab">
      <svg width="276" height="34" viewBox="0 0 276 34" aria-hidden="true"><polygon points="14,0 276,0 262,34 0,34" fill="var(--tab-blue)"/></svg>
      <span>Web: www.zelvora-example.com.au</span>
    </div>
  </section>

</main>
</body>
</html>
```